Business card to promote business guidance

I need a card design to give to all my customers advertising a way to build a business exactly like the one they just bought from. I have an online store and will include one with each shipment. It should state the way to financial freedom and working for yourself

Target Market(s)

Young Entrepreneurs that want to start and don't know how

Industry/Entity Type

Business

Contact Information for Business Card

"You just bought from a successful company on Brindlemart. I have a unique business model, discovered by me, unlike any other that can make anyone successful. Follow me and message me for exactly the same model. If you ever wanted to work for yourself, I will teach you how. It's not a pipe dream, allow me to guide you out of the box."

Colors
85abd2

Requirements
Must have
• website www.dorianwelkby.example
instagram @thedorianwelkby

```html
<!DOCTYPE html>
<html lang="en">
<head>
<meta charset="UTF-8">
<title>Business Guidance Card</title>
<link href="https://fonts.googleapis.com/css2?family=Montserrat:wght@800&family=Manrope:wght@300;400&family=Archivo:wght@800&display=swap" rel="stylesheet">
<style>
  :root {
    --backdrop: #c4c9d1;
    --card: #000000;
    --white: #ffffff;
    --blue: #85abd2;
    --grey: #cfcfcf;
  }
  html, body {
    margin: 0;
    padding: 0;
    width: 1200px;
    height: 1000px;
    overflow: hidden;
    background: var(--backdrop);
  }
  .card {
    position: absolute;
    left: 360px;
    top: 80px;
    width: 480px;
    height: 842px;
    background: var(--card);
  }
  .card > * { position: absolute; margin: 0; }
  .intro {
    left: 0; width: 100%;
    text-align: center;
    font-family: "Manrope", sans-serif;
    font-weight: 300;
    color: var(--blue);
    font-size: 19px;
    line-height: 27px;
    top: 16px;
  }
  .headline {
    font-family: "Montserrat", sans-serif;
    font-weight: 800;
    font-size: 29px;
    letter-spacing: 0.13em;
    line-height: 34px;
    text-transform: uppercase;
  }
  .white { color: var(--white); }
  .blue { color: var(--blue); }
  .sub {
    font-family: "Manrope", sans-serif;
    font-weight: 400;
    font-size: 20px;
    letter-spacing: 0.04em;
    line-height: 34px;
    color: var(--blue);
    text-transform: uppercase;
  }
  .follow-box {
    left: 53px; top: 333px;
    width: 374px; height: 98px;
    border: 2px solid var(--white);
    box-sizing: border-box;
  }
  .follow-lead {
    left: 64px; top: 340px;
    font-family: "Manrope", sans-serif;
    font-weight: 300;
    font-size: 20px;
    color: var(--blue);
  }
  .contact {
    left: 0; width: 100%;
    top: 448px;
    text-align: center;
    font-family: "Manrope", sans-serif;
    font-weight: 300;
    font-size: 19px;
    line-height: 26px;
    color: var(--grey);
  }
  .teach {
    left: 25px; top: 632px;
    font-family: "Archivo", sans-serif;
    font-weight: 800;
    font-size: 20px;
    color: var(--white);
  }
  .dream-box {
    left: 25px; top: 680px;
    width: 430px; height: 122px;
    border: 2px solid var(--white);
    box-sizing: border-box;
  }
  .dream-line {
    left: 36px; top: 688px;
    font-family: "Montserrat", sans-serif;
    font-weight: 800;
    font-size: 24px;
    letter-spacing: 0.1em;
    color: var(--blue);
  }
  .dream-line .lead {
    font-family: "Manrope", sans-serif;
    font-weight: 400;
    letter-spacing: 0;
    font-size: 21px;
  }
  .allow {
    left: 36px; top: 722px;
    font-family: "Manrope", sans-serif;
    font-size: 21px;
    color: var(--white);
  }
  .guide {
    left: 36px; top: 750px;
  }
  .guide span { background: var(--card); padding-right: 2px; }
</style>
</head>
<body>
  <main class="card">
    <p class="intro">You just bought from a<br>SUCCESSFUL COMPANY ON BRINDLEMART</p>

    <p class="headline white" style="left:25px; top:95px;">I have a unique<br>business model,</p>
    <p class="sub" style="left:25px; top:163px;">Discovered by me,<br>unlike any other,</p>
    <p class="headline white" style="left:25px; top:233px;">That can make<br>anyone successful.</p>

    <div class="follow-box"></div>
    <p class="follow-lead">Follow me and message me</p>
    <p class="headline blue" style="left:64px; top:364px; font-size:27px; line-height:31px;">For exactly the<br>same model<span class="white">.</span></p>

    <p class="contact">www.dorianwelkby.example<br>@thedorianwelkby</p>

    <p class="headline blue" style="left:25px; top:528px;">If you ever<br>wanted to work<br>for yourself,</p>
    <p class="teach">I WILL TEACH YOU HOW</p>

    <div class="dream-box"></div>
    <p class="dream-line"><span class="lead">IT’S</span> NOT A PIPE DREAM<span class="white">,</span></p>
    <p class="allow">allow me to</p>
    <p class="headline white guide"><span>Guide you out of</span><br><span>the box.</span></p>
  </main>
</body>
</html>
```